Business Card for Pottery and Jewellery Designer

A new business card design is needed to accompany a newly launching pottery and jewellery website. The company logo has been attached for use. The company is called Glazewick Studio. For a sense of the vibe please see the website (it is currently under construction but this way you'll get a feel for the style) www.GlazewickStudio.com

The website font is Pontano Sans for the body of the text with Overlock for headers.

The overall look should be clean and elegant. The back side can have just the logo. The front side should have a smaller logo and the following details displayed:

Glazewick Studio
Designer: Hollis Marrow
Phone: xxx.xxx.xxxx
Email: Designer@GlazewickStudio.com

The structure of displaying this is completely up to you. Different layouts and creative methods of displaying contact info are welcome as long as it stays clean/uncluttered.

No product photographs are to be included in the design as the catalogue changes quickly.

Colour preferences lean towards elegant and understated (charcoal grey, dark navy blue etc.)

Please let me know if you have any further questions or further details required.

Target Market(s)

Target market is 30+ year old women

Industry/Entity Type

Construction

Colors
ffffff
1b1b1b
474747
d9d9d9
fafafa
0355a3

Requirements
Must have
• The submissions so far have looked very typical and don't stand out right now. They're also all in navy with very little variation. I'm looking for something that stands out a it more while still being clean-looking.
Nice to have
• I've attached a few design samples and an idea for a backdrop. It would be great to see some designs in black, white, and grey with only a hint of color.
Should not have
• Product Images

```html
<!DOCTYPE html>
<html lang="en">
<head>
<meta charset="utf-8">
<title>Glazewick Studio – Business Card</title>
<link href="https://fonts.googleapis.com/css2?family=Overlock:wght@400;700&family=Pontano+Sans&display=swap" rel="stylesheet">
<style>
  :root{
    --page:#ececee;
    --card-white:#fafafa;
    --charcoal:#1b1b1b;
    --graphite:#474747;
    --mist:#d9d9d9;
    --white:#ffffff;
    --accent:#0355a3;
  }
  html,body{margin:0;padding:0;width:1200px;height:1023px;overflow:hidden;background:var(--page);}
  .canvas{position:relative;width:1200px;height:1023px;}
  .card{position:absolute;top:357px;width:540px;height:309px;border-radius:16px;overflow:hidden;
        box-shadow:0 6px 18px rgba(0,0,0,.18);}
  .card-front{left:40px;background:var(--card-white);}
  .card-back{left:620px;background:radial-gradient(ellipse at 35% 60%, #4a4a4a 0%, #2c2c2c 55%, var(--charcoal) 100%);}

  .brand{position:absolute;left:34px;top:40px;display:flex;align-items:center;gap:12px;}
  .brand-dot{width:30px;height:30px;border-radius:50%;background:var(--accent);}
  .brand-name{font-family:"Overlock",sans-serif;font-weight:400;font-size:30px;line-height:1;letter-spacing:.5px;
              text-transform:uppercase;color:var(--charcoal);white-space:nowrap;}

  .person{position:absolute;left:34px;bottom:56px;}
  .person-name{font-family:"Overlock",sans-serif;font-size:19px;text-transform:uppercase;color:var(--charcoal);letter-spacing:.5px;}
  .person-role{font-family:"Pontano Sans",sans-serif;font-size:12px;color:var(--graphite);margin-top:3px;}

  .divider{position:absolute;left:232px;top:150px;width:80px;height:1px;
           background:linear-gradient(90deg,transparent,var(--graphite),transparent);transform:rotate(18deg);}

  .contact{position:absolute;left:318px;top:108px;list-style:none;margin:0;padding:0;}
  .contact li{display:flex;align-items:center;gap:7px;font-family:"Pontano Sans",sans-serif;
              font-size:12.5px;color:var(--graphite);line-height:21px;white-space:nowrap;}
  .contact svg{width:13px;height:13px;flex:none;}

  .edge-rule{position:absolute;left:0;right:0;bottom:24px;height:3px;background:var(--accent);}
  .edge-band{position:absolute;left:0;right:0;bottom:0;height:18px;background:linear-gradient(180deg,var(--graphite),var(--charcoal));}

  .back-mark{position:absolute;inset:0;display:flex;align-items:center;justify-content:center;gap:16px;}
  .back-dot{width:46px;height:46px;border-radius:50%;background:var(--accent);}
  .back-name{font-family:"Overlock",sans-serif;font-size:34px;line-height:1;text-transform:uppercase;color:var(--white);letter-spacing:1px;white-space:nowrap;}
</style>
</head>
<body>
<main class="canvas">
  <section class="card card-front" aria-label="Card front">
    <div class="brand">
      <span class="brand-dot"></span>
      <span class="brand-name">Glazewick Studio</span>
    </div>
    <div class="divider"></div>
    <ul class="contact">
      <li>
        <svg viewBox="0 0 16 16"><path fill="var(--charcoal)" d="M3 1h3l1.5 4-2 1.3a8 8 0 0 0 4.2 4.2L11 8.5l4 1.5v3a2 2 0 0 1-2 2C7 15 1 9 1 3a2 2 0 0 1 2-2z"/></svg>
        (555) 555.0142
      </li>
      <li>
        <svg viewBox="0 0 16 16"><rect x="1" y="3" width="14" height="10" rx="1" fill="var(--charcoal)"/><path d="M1.5 3.5 8 9l6.5-5.5" stroke="var(--white)" stroke-width="1.2" fill="none"/></svg>
        Designer@GlazewickStudio.com
      </li>
      <li>
        <svg viewBox="0 0 16 16"><circle cx="8" cy="8" r="7" fill="var(--charcoal)"/><path d="M1 8h14M8 1c3 3.5 3 10.5 0 14M8 1c-3 3.5-3 10.5 0 14" stroke="var(--white)" stroke-width="1" fill="none"/></svg>
        www.GlazewickStudio.com
      </li>
    </ul>
    <div class="person">
      <div class="person-name">Hollis Marrow</div>
      <div class="person-role">Designer</div>
    </div>
    <div class="edge-rule"></div>
    <div class="edge-band"></div>
  </section>

  <section class="card card-back" aria-label="Card back">
    <div class="back-mark">
      <span class="back-dot"></span>
      <span class="back-name">Glazewick Studio</span>
    </div>
  </section>
</main>
</body>
</html>
```